Corvanta512 Business Card Redesign

I want to create a design for brand new business cards, I need something exceptional for clear plastic business card design. Please do not submit without it being on a clear design. Photos of the various logo versions attached.

```html
<!DOCTYPE html>
<html lang="en">
<head>
<meta charset="utf-8">
<title>Corvanta512 Business Card</title>
<link href="https://fonts.googleapis.com/css2?family=Michroma&family=Poppins:wght@400;500;600&display=swap" rel="stylesheet">
<style>
  :root {
    --page: #ffffff;
    --card-light: #3f3863;
    --card-mid: #2b2648;
    --card-dark: #14122a;
    --gold-light: #f3dc98;
    --gold: #dcbc6c;
    --gold-deep: #b58d3d;
    --ink-on-gold: #2a2344;
    --white: #ffffff;
    --rule: rgba(200, 190, 230, 0.45);
  }
  * { margin: 0; padding: 0; box-sizing: border-box; }
  html, body { width: 1200px; height: 2333px; overflow: hidden; background: var(--page); }
  .canvas { position: relative; width: 1200px; height: 2333px; }

  .card {
    position: absolute;
    left: 83px;
    width: 1034px;
    height: 592px;
    overflow: hidden;
    background:
      radial-gradient(ellipse 60% 75% at 50% 20%, var(--card-light) 0%, var(--card-mid) 55%, var(--card-dark) 100%);
    color: var(--white);
  }
  .card--front { top: 540px; }
  .card--back { top: 1212px; }

  .brand { position: absolute; display: flex; flex-direction: column; align-items: center; }
  .brand__mark {
    border-radius: 50%;
    background: linear-gradient(145deg, var(--gold-light), var(--gold-deep));
  }
  .brand__name {
    font-family: "Michroma", sans-serif;
    color: var(--gold);
    white-space: nowrap;
  }
  .card--front .brand { left: 0; right: 0; top: 72px; }
  .card--front .brand__mark { width: 150px; height: 150px; }
  .card--front .brand__name { font-size: 40px; margin-top: 28px; }

  .services { position: absolute; top: 338px; left: 78px; width: 878px; display: flex; }
  .service { flex: 1; display: flex; flex-direction: column; align-items: center; position: relative; }
  .service + .service::before {
    content: ""; position: absolute; left: 0; top: -12px; height: 112px; width: 2px;
    background: linear-gradient(to bottom, transparent, var(--gold-deep), transparent);
  }
  .service svg { width: 70px; height: 62px; }
  .service__label {
    margin-top: 14px;
    font-family: "Michroma", sans-serif;
    font-size: 21px;
    color: var(--gold);
    letter-spacing: 0.5px;
  }

  .front-site {
    position: absolute; top: 482px; left: 0; right: 0; text-align: center;
    font-family: "Poppins", sans-serif; font-weight: 600; font-size: 26px; letter-spacing: 11px;
  }
  .front-site .accent { color: var(--gold); }

  .person { position: absolute; left: 116px; top: 112px; }
  .person__name {
    font-family: "Michroma", sans-serif; font-size: 46px; color: var(--gold); line-height: 1;
  }
  .person__role {
    font-family: "Poppins", sans-serif; font-size: 23px; letter-spacing: 3px; margin: 8px 0 0 30px;
  }
  .card--back .brand { left: 720px; width: 220px; top: 92px; }
  .card--back .brand__mark { width: 100px; height: 100px; }
  .card--back .brand__name { font-size: 26px; margin-top: 22px; }

  .divider { position: absolute; left: 100px; top: 360px; width: 836px; height: 1px; background: var(--rule); }

  .contact { position: absolute; top: 386px; font-family: "Poppins", sans-serif; font-size: 25px; font-weight: 500; }
  .contact--phones { left: 110px; }
  .contact--web { left: 578px; }
  .contact__row { display: flex; align-items: center; gap: 10px; height: 40px; }
  .contact__row svg { width: 22px; height: 22px; flex: none; }
  .pill {
    display: inline-block; margin-top: 6px; padding: 4px 17px; border-radius: 14px;
    background: linear-gradient(180deg, var(--gold-light), var(--gold));
    color: var(--ink-on-gold); font-weight: 600; font-size: 25px; white-space: nowrap;
  }
</style>
</head>
<body>
<main class="canvas">

  <section class="card card--front">
    <div class="brand">
      <div class="brand__mark"></div>
      <div class="brand__name">Corvanta512</div>
    </div>

    <div class="services">
      <div class="service">
        <svg viewBox="0 0 70 62" aria-hidden="true">
          <g fill="var(--gold)">
            <rect x="30" y="2" width="16" height="32" rx="3" transform="rotate(45 38 18)"/>
            <rect x="34" y="22" width="8" height="30" rx="2" transform="rotate(-45 38 37)"/>
            <rect x="8" y="44" width="30" height="6" rx="2"/>
            <rect x="4" y="52" width="38" height="7" rx="2"/>
          </g>
        </svg>
        <span class="service__label">LEGAL</span>
      </div>
      <div class="service">
        <svg viewBox="0 0 70 62" aria-hidden="true">
          <path fill="var(--gold)" d="M35 60 C10 42 2 32 2 19 C2 8 10 2 19 2 C26 2 31 6 35 11 C39 6 44 2 51 2 C60 2 68 8 68 19 C68 32 60 42 35 60Z"/>
          <path fill="var(--card-mid)" d="M30 16h10v9h9v10h-9v9H30v-9h-9V25h9z"/>
        </svg>
        <span class="service__label">MEDICAL</span>
      </div>
      <div class="service">
        <svg viewBox="0 0 70 62" aria-hidden="true">
          <g fill="var(--gold)">
            <rect x="18" y="4" width="36" height="30" rx="8"/>
            <rect x="22" y="30" width="26" height="16" rx="4"/>
            <rect x="10" y="44" width="22" height="14" rx="4" transform="rotate(-20 21 51)"/>
            <rect x="38" y="44" width="22" height="14" rx="4" transform="rotate(20 49 51)"/>
          </g>
          <g stroke="var(--card-mid)" stroke-width="2">
            <line x1="27" y1="6" x2="27" y2="20"/><line x1="36" y1="6" x2="36" y2="20"/><line x1="45" y1="6" x2="45" y2="20"/>
          </g>
        </svg>
        <span class="service__label">SUPPORT</span>
      </div>
      <div class="service">
        <svg viewBox="0 0 70 62" aria-hidden="true">
          <path fill="var(--gold)" d="M35 2 L62 10 V30 C62 45 50 55 35 60 C20 55 8 45 8 30 V10Z"/>
          <path fill="none" stroke="var(--card-mid)" stroke-width="6" stroke-linecap="round" stroke-linejoin="round" d="M23 31 L32 40 L48 22"/>
        </svg>
        <span class="service__label">INSURANCE</span>
      </div>
    </div>

    <p class="front-site">www.<span class="accent">corvanta512</span>.com</p>
  </section>

  <section class="card card--back">
    <div class="person">
      <h1 class="person__name">Jhon Doe</h1>
      <p class="person__role">Consultant</p>
    </div>

    <div class="brand">
      <div class="brand__mark"></div>
      <div class="brand__name">Corvanta512</div>
    </div>

    <div class="divider"></div>

    <div class="contact contact--phones">
      <div class="contact__row">
        <svg viewBox="0 0 24 24" aria-hidden="true"><path fill="var(--gold)" d="M6.6 10.8a15.1 15.1 0 006.6 6.6l2.2-2.2c.3-.3.7-.4 1-.2 1.1.4 2.3.6 3.6.6.6 0 1 .4 1 1V20c0 .6-.4 1-1 1A17 17 0 013 4c0-.6.4-1 1-1h3.5c.6 0 1 .4 1 1 0 1.3.2 2.5.6 3.6.1.3 0 .7-.2 1z"/></svg>
        <span>(833) CRVN-512</span>
      </div>
      <div class="contact__row">
        <svg viewBox="0 0 24 24" aria-hidden="true"><path fill="var(--gold)" d="M6.6 10.8a15.1 15.1 0 006.6 6.6l2.2-2.2c.3-.3.7-.4 1-.2 1.1.4 2.3.6 3.6.6.6 0 1 .4 1 1V20c0 .6-.4 1-1 1A17 17 0 013 4c0-.6.4-1 1-1h3.5c.6 0 1 .4 1 1 0 1.3.2 2.5.6 3.6.1.3 0 .7-.2 1z"/></svg>
        <span>1-833-2786-512</span>
      </div>
      <span class="pill">24/7 Free Consultation</span>
    </div>

    <div class="contact contact--web">
      <div class="contact__row">
        <svg viewBox="0 0 24 24" aria-hidden="true"><g fill="none" stroke="var(--gold)" stroke-width="1.6"><circle cx="12" cy="12" r="9"/><ellipse cx="12" cy="12" rx="4" ry="9"/><line x1="3" y1="12" x2="21" y2="12"/><line x1="4.5" y1="7.5" x2="19.5" y2="7.5"/><line x1="4.5" y1="16.5" x2="19.5" y2="16.5"/></g></svg>
        <span>www.corvanta512.com</span>
      </div>
      <div class="contact__row">
        <svg viewBox="0 0 24 24" aria-hidden="true"><rect x="2" y="5" width="20" height="14" rx="1.5" fill="var(--gold)"/><path d="M2.5 6 L12 13 L21.5 6" fill="none" stroke="var(--card-mid)" stroke-width="1.6"/></svg>
        <span>info@corvanta512.com</span>
      </div>
      <span class="pill">We'll respond within 24 hours</span>
    </div>
  </section>

</main>
</body>
</html>
```